Moderne Visitenkarten für Medizintechnikfirma
Zielgruppe
Vertriebsfirma von moderner und innovativer Medizintechnik
Zielgruppe: Ärzte, Kliniken, Medizintechnikfirmen, Patienten
Aufgabenstellung
Besonderes, modernes, auffälliges und ansprechendes Design ohne überladen oder aufdringlich zu sein
Farbenorientierung kann am Logo und der Website geschehen. Wenn zum Logo harmonierend, sind aber auch andere Farben gerne gesehen.
Format: eher horizontal, vertikal aber auch möglich, abgerundete Ecken einplanen
Wenn möglich folgende Infos bitte schon auf die Karten bringen (pro Person eine Karte):
Harald Zumbrink (CEO)
harald.zumbrink@vitalnova-partner.de
(VitalNova Partner GmbH
Lärchenstraße 14
49377 Fallrode)
www.vitalnova-partner.de
info@vitalnova-partner.de
Jannik Sprau (CoS)
jannik.sprau@vitalnova-partner.de
Die allgemeinen Firmeninfos können deutlich kleiner sein. Anschrift nur wenn es dadurch nicht zu viel werden würde.

```html
<!DOCTYPE html>
<html lang="de">
<head>
<meta charset="utf-8">
<title>VitalNova Partner – Visitenkarten</title>
<link rel="stylesheet" href="https://fonts.googleapis.com/css2?family=Montserrat:wght@400;500;600&display=swap">
<style>
  :root {
    --stage: #1c1c1c;
    --purple: #3f1f7a;
    --purple-deep: #2a1559;
    --purple-ink: #351a78;
    --red: #f21c06;
    --white: #ffffff;
    --grey-text: #3c3c3c;
    --grey-soft: #6a6a6a;
  }
  * { box-sizing: border-box; margin: 0; padding: 0; }
  html, body { width: 1200px; height: 1200px; overflow: hidden; }
  body {
    background: var(--stage);
    font-family: "Montserrat", sans-serif;
    position: relative;
  }
  .card {
    position: absolute;
    left: 230px;
    width: 740px;
    height: 478px;
    border-radius: 14px;
    overflow: hidden;
    box-shadow: 0 14px 40px rgba(0,0,0,.45);
  }
  .card--back {
    top: 95px;
    background: linear-gradient(120deg, var(--purple-deep) 0%, var(--purple) 55%, #45237f 100%);
    color: var(--white);
  }
  .card--front {
    top: 625px;
    background: var(--white);
    color: var(--grey-text);
  }
  .brand {
    position: absolute;
    left: 0; right: 0;
    display: flex;
    align-items: center;
    justify-content: center;
    gap: 16px;
  }
  .brand__dot {
    width: 36px; height: 36px; border-radius: 50%;
    flex: none;
  }
  .brand__name {
    font-weight: 600;
    font-size: 42px;
    letter-spacing: .5px;
    line-height: 1;
  }
  .card--back .brand { top: 88px; }
  .card--back .brand__dot { background: var(--white); }
  .card--front .brand { top: 80px; }
  .card--front .brand__dot { background: var(--purple-ink); }
  .card--front .brand__name { color: var(--purple-ink); }

  .info {
    position: absolute;
    font-size: 17px;
    font-weight: 500;
    font-style: normal;
    letter-spacing: 1.2px;
    line-height: 1.5;
  }
  .info--address { left: 90px; bottom: 62px; }
  .info--online { left: 400px; bottom: 62px; }

  .person {
    position: absolute;
    top: 205px; left: 0; right: 0;
    text-align: center;
  }
  .person__name { font-size: 34px; font-weight: 500; color: var(--grey-text); letter-spacing: .5px; }
  .person__role { font-size: 17px; font-weight: 500; color: var(--grey-soft); margin-top: 2px; }
  .contact {
    position: absolute;
    top: 318px; left: 215px;
    font-size: 17px;
    letter-spacing: 1px;
    line-height: 1.55;
    color: var(--grey-text);
  }
  .band {
    position: absolute;
    left: 0; right: 0; bottom: 0;
    height: 60px;
    background: var(--red);
  }
</style>
</head>
<body>
  <section class="card card--back" aria-label="Kartenrückseite">
    <div class="brand">
      <span class="brand__dot"></span>
      <div class="brand__name">VitalNova Partner</div>
    </div>
    <address class="info info--address">
      VitalNova Partner GmbH<br>
      Lärchenstraße 14<br>
      49377 Fallrode
    </address>
    <div class="info info--online">
      www.vitalnova-partner.de<br>
      info@vitalnova-partner.de<br>
      0800-5318207
    </div>
  </section>

  <section class="card card--front" aria-label="Kartenvorderseite">
    <div class="brand">
      <span class="brand__dot"></span>
      <div class="brand__name">VitalNova Partner</div>
    </div>
    <div class="person">
      <div class="person__name">Harald Zumbrink</div>
      <div class="person__role">CEO</div>
    </div>
    <div class="contact">
      +4915209847362<br>
      harald.zumbrink@vitalnova-partner.de
    </div>
    <div class="band"></div>
  </section>
</body>
</html>
```